Refrigeration & Air Conditioning modern and appealing

We want to design a business card that is modern and appealing using existing logo supplied

Front card
Residential Commercial Diary
RTA : AU052731
Licence L287456

Back card
Warren Kostig
Director
0491 357 208
info@frostlinerefrigeration.com.au
www.frostlinerefrigeration.com.au
• Air Conditioning
• Cool Rooms & Refrigeration
• Installation
• Service & Repair
• Preventative Maintenance

We offer 24/7 emergency service

```html
<!DOCTYPE html>
<html lang="en">
<head>
<meta charset="utf-8">
<title>Frostline Business Cards</title>
<link rel="stylesheet" href="https://fonts.googleapis.com/css2?family=Montserrat:wght@400;500;700;800&display=swap">
<style>
  :root {
    --bg: #c9c9cc;
    --card: #121213;
    --white: #ffffff;
    --purple: #a25cf0;
    --lilac: #b9a3f5;
    --muted: #e6e6ea;
  }
  * { margin: 0; padding: 0; box-sizing: border-box; }
  html, body { width: 1200px; height: 939px; overflow: hidden; }
  body {
    background: radial-gradient(ellipse at 50% 45%, #e4e4e6 0%, var(--bg) 60%, #b4b4b8 100%);
    font-family: "Montserrat", sans-serif;
    color: var(--white);
    position: relative;
  }
  .card {
    position: absolute;
    width: 540px;
    height: 309px;
    background: var(--card);
    box-shadow: 0 10px 24px rgba(0,0,0,0.35);
  }
  .card-front { left: 110px; top: 90px; }
  .card-back { left: 550px; top: 520px; }

  /* front */
  .brand {
    position: absolute;
    left: 0; right: 0; top: 108px;
    display: flex; align-items: center; justify-content: center; gap: 14px;
  }
  .brand-dot {
    width: 34px; height: 34px; border-radius: 50%;
    background: var(--purple);
  }
  .brand-name {
    font-weight: 800; font-size: 46px; letter-spacing: 1px;
    color: var(--white);
  }
  .front-details {
    position: absolute; left: 0; right: 0; bottom: 34px;
    display: flex; justify-content: center; align-items: center; gap: 8px;
    font-size: 12.5px; font-weight: 400; color: var(--muted);
  }
  .sep { width: 3px; height: 14px; background: var(--purple); }

  /* back */
  .back-brand {
    position: absolute; left: 34px; top: 76px; width: 170px;
    display: flex; align-items: center; gap: 10px;
  }
  .back-brand .brand-dot { width: 22px; height: 22px; }
  .back-brand .brand-name { font-size: 26px; }
  .divider {
    position: absolute; left: 218px; top: 34px; width: 1px; height: 148px;
    background: #9a9a9f;
  }
  .contact { position: absolute; left: 236px; top: 34px; }
  .person-name {
    font-weight: 800; font-size: 24px; letter-spacing: 0.5px;
    color: var(--lilac); text-transform: uppercase;
  }
  .person-role { font-size: 13px; margin: 2px 0 14px 16px; }
  .contact-list { list-style: none; margin-left: 34px; }
  .contact-list li {
    display: flex; align-items: center; gap: 8px;
    font-size: 13px; margin-bottom: 7px;
  }
  .contact-list svg { width: 13px; height: 13px; flex: none; }
  .services {
    position: absolute; left: 0; right: 0; bottom: 28px;
    text-align: center; font-size: 13.5px; line-height: 1.45;
  }
  .services .offer {
    color: var(--purple); font-weight: 700; font-size: 14px;
    text-transform: uppercase; letter-spacing: 0.3px; margin-bottom: 2px;
  }
</style>
</head>
<body>

<section class="card card-front" aria-label="Business card front">
  <div class="brand">
    <span class="brand-dot"></span>
    <span class="brand-name">FROSTLINE</span>
  </div>
  <p class="front-details">
    <span>RTA : AU052731</span><span class="sep"></span>
    <span>Residential Commercial Diary</span><span class="sep"></span>
    <span>Licence L287456</span>
  </p>
</section>

<section class="card card-back" aria-label="Business card back">
  <div class="back-brand">
    <span class="brand-dot"></span>
    <span class="brand-name">FROSTLINE</span>
  </div>
  <div class="divider"></div>
  <div class="contact">
    <p class="person-name">Warren Kostig</p>
    <p class="person-role">Director</p>
    <ul class="contact-list">
      <li>
        <svg viewBox="0 0 24 24"><path fill="#a25cf0" d="M6.6 10.8a15 15 0 0 0 6.6 6.6l2.2-2.2a1 1 0 0 1 1-.25 11.4 11.4 0 0 0 3.6.57 1 1 0 0 1 1 1V20a1 1 0 0 1-1 1A17 17 0 0 1 3 4a1 1 0 0 1 1-1h3.5a1 1 0 0 1 1 1c0 1.25.2 2.45.57 3.57a1 1 0 0 1-.25 1z"/></svg>
        0491 357 208
      </li>
      <li>
        <svg viewBox="0 0 24 24"><rect x="2" y="5" width="20" height="14" rx="1" fill="#a25cf0"/><path d="M2 6l10 7 10-7" fill="none" stroke="#121213" stroke-width="2"/></svg>
        info@frostlinerefrigeration.com.au
      </li>
      <li>
        <svg viewBox="0 0 24 24" fill="none" stroke="#a25cf0" stroke-width="2"><circle cx="12" cy="12" r="9"/><path d="M3 12h18M12 3c3 3 3 15 0 18M12 3c-3 3-3 15 0 18"/></svg>
        www.frostlinerefrigeration.com.au
      </li>
    </ul>
  </div>
  <div class="services">
    <p class="offer">We offer 24/7 emergency service</p>
    <p>• Air Conditioning • Cool Rooms &amp; Refrigeration • Installation</p>
    <p>• Service &amp; Repair • Preventative Maintenance</p>
  </div>
</section>

</body>
</html>
```